Nobody Left the Lantern Burning - Tom Halvery - CD Cover Design Project

Single Cover for CD & Online media e.g. Tunebox Graphics
The first song release from Tom Halvery will be the track 'Nobody Left the Lantern Burning'.
For the release the single requires artwork that is eye catching, seriously professional & meets the requirements of Disc Sprout, Tunebox and also a physical copy on CD.
Track listings for CD will be:
1. Nobody Left the Lantern Burning
2. Nobody Left the Lantern Burning - Instrumental
see details in this link:
http://members.discsprout-example.com/faq.aspx
http://selfmadesound.discsprout-example.com/2009/11/avoid-album-art-atrocities/
http://answers.quorvex-example.com/question/index?qid=20111015141433AAdDTmH
Any advice on this would be greatly appreciated,
I would also like the two logo's I have uploaded to be used,
one is the Tom Halvery logo and the other is for Milbrook & Tandy Records logo (please remove the R and replace with a C for copyright.)
There are four high res photo shopped pictures of Tom Halvery and another zip file of many others, it would be nice to include one of these maybe on the 2nd page or back of the CD. Please don't use them as the front cover.
I imagine an Art Deco illustration but please listen to the track and let it inspire you.
Good Luck
Updates
I don't feel this is what I'm looking for, the design needs to refelct a broken heart without being a picture of a broken heart
Reason: No design has been what we are after so far so the deadline has been extended and the budget increased.

```html
<!DOCTYPE html>
<html lang="en">
<head>
<meta charset="utf-8">
<title>Nobody Left the Lantern Burning – Tom Halvery</title>
<link href="https://fonts.googleapis.com/css2?family=Lato:wght@400;700&family=Crimson+Text:wght@400&display=swap" rel="stylesheet">
<style>
  :root {
    --paper: #fbfbf5;
    --haze-green: #e6ecd2;
    --haze-gold: #f3e3a4;
    --halo-gold: #e9b83a;
    --halo-bronze: #9c6a24;
    --heart-red: #e8432a;
    --heart-deep: #b8281a;
    --ink: #0b0908;
    --label-white: #f4f1ea;
    --label-gold: #e3c13a;
    --title-red: #9e1512;
  }
  html, body {
    margin: 0;
    padding: 0;
    width: 1200px;
    height: 1200px;
    overflow: hidden;
    background: var(--paper);
  }
  .cover {
    position: relative;
    width: 1200px;
    height: 1200px;
    overflow: hidden;
    background: var(--paper);
  }
  .cover-art {
    position: absolute;
    inset: 0;
    width: 1200px;
    height: 1200px;
  }
  .label {
    position: absolute;
    margin: 0;
    white-space: nowrap;
  }
  .artist-name {
    left: 660px;
    top: 718px;
    width: 470px;
    font-family: "Lato", sans-serif;
    font-weight: 400;
    font-size: 44px;
    letter-spacing: 0.18em;
    line-height: 64px;
    text-align: center;
    color: var(--label-white);
  }
  .title-lead {
    left: 78px;
    top: 910px;
    width: 560px;
    font-family: "Lato", sans-serif;
    font-weight: 400;
    font-size: 34px;
    letter-spacing: 0.16em;
    line-height: 60px;
    text-align: center;
    color: var(--label-gold);
  }
  .title-main {
    left: 170px;
    top: 1010px;
    width: 940px;
    font-family: "Crimson Text", serif;
    font-weight: 400;
    font-size: 128px;
    line-height: 160px;
    text-align: center;
    color: var(--title-red);
  }
</style>
</head>
<body>
<main class="cover">
  <svg class="cover-art" viewBox="0 0 1200 1200" xmlns="http://www.w3.org/2000/svg">
    <defs>
      <radialGradient id="haze" cx="50%" cy="38%" r="65%">
        <stop offset="0%" stop-color="var(--haze-gold)"/>
        <stop offset="45%" stop-color="var(--haze-green)"/>
        <stop offset="100%" stop-color="var(--paper)"/>
      </radialGradient>
      <radialGradient id="halo" cx="50%" cy="50%" r="50%">
        <stop offset="0%" stop-color="var(--halo-bronze)"/>
        <stop offset="55%" stop-color="var(--halo-gold)"/>
        <stop offset="100%" stop-color="var(--haze-gold)" stop-opacity="0.6"/>
      </radialGradient>
      <linearGradient id="heart" x1="0" y1="0" x2="1" y2="1">
        <stop offset="0%" stop-color="var(--heart-red)"/>
        <stop offset="100%" stop-color="var(--heart-deep)"/>
      </linearGradient>
    </defs>

    <rect class="backdrop-texture" x="0" y="0" width="1200" height="1200" fill="url(#haze)"
          role="img" aria-label="Soft abstract painted texture in pale green and gold"/>

    <circle class="halo-figure" cx="580" cy="335" r="290" fill="url(#halo)"
            role="img" aria-label="Illustration of a crouching figure on a pedestal inside a spiked sun halo"/>

    <g class="pedestal" fill="var(--ink)">
      <polygon points="282,378 740,388 728,420 296,412"/>
      <rect x="292" y="412" width="26" height="500"/>
      <rect x="410" y="412" width="16" height="520"/>
      <rect x="598" y="418" width="16" height="300"/>
      <rect x="700" y="420" width="24" height="290"/>
    </g>

    <rect class="fallen-heart" x="440" y="540" width="290" height="250" rx="40" fill="url(#heart)"
          role="img" aria-label="Illustration of a red heart held by the figure"/>

    <g class="hanging-lines" stroke="var(--ink)" stroke-width="3">
      <line x1="22" y1="0" x2="24" y2="1200"/>
      <line x1="36" y1="0" x2="36" y2="1200"/>
      <line x1="142" y1="0" x2="150" y2="1200"/>
      <line x1="168" y1="0" x2="210" y2="1200" stroke-width="2"/>
      <line x1="250" y1="0" x2="258" y2="1200"/>
      <line x1="978" y1="0" x2="990" y2="1200"/>
      <line x1="1026" y1="0" x2="1014" y2="1200" stroke-width="2"/>
      <line x1="1076" y1="0" x2="1080" y2="1200"/>
      <line x1="1137" y1="0" x2="1150" y2="1200" stroke-width="4"/>
    </g>

    <g class="label-plates" fill="var(--ink)">
      <polygon points="645,712 1147,706 1140,792 652,796"/>
      <polygon points="66,904 654,900 648,978 72,982"/>
      <polygon points="160,998 1120,990 1126,1200 154,1200"/>
    </g>
  </svg>

  <p class="label artist-name">TOM HALVERY</p>
  <p class="label title-lead">NOBODY LEFT THE</p>
  <h1 class="label title-main">Lantern Burning</h1>
</main>
</body>
</html>
```